Talvoro Web Design

We need a redesign of our current website www.talvoro-example.com

THIS IS A DESIGN STAGE ONLY

We have attached details of the whole project for your understanding only

We do not want to change our Logo but do want to have a more modern and intuitive feel to the site.

The first stage is the design but we are also looking for a coder to take the site to the next level

Talvoro has a current website that has been in operation for the past 6 years the design was based around the Saas self-service model and while functional does not meet Talvoro needs with regard to the new positioning.

We are happy to stay in Fendrix or will look at alternatives

The purpose of the redesign is to align the look and feel of the website to meet our current new brand position and to provide a access point for the delivery of new content from Blogs and white papers as well as a portal for information for our current users for gathering Tips and Tricks and access to additional resources to assist them to provide feedback and get support.

Talvoro is Australia's only PPM (Project and Portfolio Management) software provider that caters to the needs of project managers and C-level executives looking for insights into the alignment of resources to business strategy and investment decisions.

As companies gain maturity in PPM there is a need for innovation and management of change beyond just implementation of tools this is why Talvoro has evolved from being a SaaS to becoming a SwS (Software with Service) provider.

Talvoro is recognized as the tool of choice amongst program and project managers that is able to provide the user with an intuitive reliable interface that is capable of evolving and maturing to meet and exceed client requirements.

We are able to provide people at the coalface with tools that enable them to manage resources, scope, time sheeting, issues, changes and risk with excellent reporting functionality.

For C-level executives we are able to provide Business Intelligence (BI) functionality and reporting by integrating the PPM data with other business management systems such as ERP and CRM to provide a insight beyond pure PPM reporting.

We are able to provide Project Management insights from years of experience working with our clients in developing solutions that are inline with the evolution that comes with change.

Please feel free to email me on nigel.brask@talvoro-example.com if you require any further details. A Site map and a wire frame is available.

Competitor sites include

www.plonverk-example.com
www.surmoza-example.com
www.qarnitel-example.com
www.velubra-example.com
Updates

Hi All 

We are getting some great designs coming in and really appreciate all of your efforts.

Some feedback to you all is that we have a preference for cleaner designs that take into account comprehension ability. So reverse type to us looks good but doesnt always get the cut through.

We have to remember that this is a marketing site first and foremost so what we are looking for is the ability to engage with our audience and get them to start to explore. That is upto us to provide great content and what we want from the design is the ability to be be able to engage with our Audience.

For your consideration please review this info from our marketing plan

There are 3 main communication groups inthe sales process.

Users-        These are the peoplewho will be at the coal face inputting the data and using the product on adaily basis. It is key to provide them with an easy to use and functional toolthat is able to provide them with the information they are looking for easily andintuitively. They have the capacity to say yes and can push the sale decisionup the chain. They equally have the power to say No and stop the sales processin its tracks. They will have a opinion who or what they feel is the best ofbreed and will try to influence the process.

Users are split into two groups.

Group1- They will be diploma if not degree qualifiedwill be a mix of Male and female with majority aged 18 to 35 they are at thecareer development stage of their life cycle normally on an income 45k to 70kper annum. We would position these people very strongly in the “What is in itfor me”.

Group2- PM who has used a variety of tools and systemsover the years they will be pre disposed to one or more systems and has morethan likely been exposed to MSP. Usually in the 30 to 50 year old age rangewith extensive on the job experience.

KeyInfluencers- These are the people who while notactually utilizing the software need to receive information in the form ofreports etc from the system. They normally don’t have the capacity to say yesbut they most certainly can say no. They will have come from a PM or IT roleand have a strong understanding of the PM processes. Influencers will be 30 to50 years of age they are at the family development stage with strong demandsfrom work and family predominantly male but not exclusively. They would bedegree qualified and possibly have completed or looking at additional studies. Therewill be an emphasis on getting the job done right. They are very time poor and hardto communicate with and engage. While being time poor they have an affinitywith and understand the greater good.

DecisionMakers- These are our key decision makers whilethey may not have direct input into the system or processes they are at the endof the day the people who approve the expenditure.

There is a huge demand for this person’stime with a multitude of people from internal employees and management,suppliers, customers, the community and potential suppliers. They are oftentravelling and going from one subject matter to another meeting after meeting.They will be at the stage where children are gaining some independents or leftthe home, career is stabilized and a clear path is formed. They are very directand deal in the facts and figures when it comes to decision making, they arenormally highly educated to the MBA or Doctorate level. They will be driven byoutcomes not the process of getting there.

 

A consistent theme across this group isthe following.

Psychographics

·Values time and considers ittheir single most limited resource.

·Excited about accepting andusing innovative ideas and products always wants to be at the fore front.

·Value adding has priority overprice

·Consistent web users: preferinternet over magazines and newspapers

Behavior

·They are leaders in productselection and respond to the opinions of the ‘Industry Experts’ when makingpurchase decisions.

·This group will look to theinternet to acquire the information

·Will make an informed decisionto purchase after due consideration.

·This group can be a powerfulsales force resulting from the referral network they build and use

Hope this helps

Hi All

Sorry for the delay we are in the final stages of decisions, so sorry we have had people away from the office who need to be involved in the process.

We will submit individual questions to those in the running and let all of the people who didnt get through this time as to why shortly.

We would like to thank you all for your efforts and submissions.

Regards

Nigel Brask 

Industry/Entity Type

Business Management

Requirements
Must have
• The scope of the website is to provide a modern functional website that is easy to navigate and provides a range of products and services to meet the needs of our potential clients and current users.

Two potential groups of viewers exist:
1. Potential Clients and users from the Project management community these would be split into 3 distinct groups. ( Please refer to Page 20 Talvoro marketing Plan)
a. Project Managers
b. Project Directors
c. Business Managers
2. Current Talvoro Users

The goal of website is to engage with the project management community reinforcing the Talvoro Brand as Software with Service the key ethos should be around the company being thought leaders and industry experts with a strong commitment to clients and the success of their Portfolio/Program Management Office

Maintaining a modern and user friendly site is of the highest importance in order to hold users attention and guide the viewer to information that will lead to a decision to pursue accreditation and association with the Talvoro Brand

We would like to guide potential clients to want to engage with us in assisting them to understand their current position in the Maturity maturity model and to use us as a source for information and guidance.

Benefits for using the site should include:
• Information from a broad spectrum of Project Management professionals and recognized industry experts.
• Information on the Talvoro Product and Services
• Timely and up to date information that encourages readers to return to the site
• Call to action, and plans for potential users of Talvoro software.
• Demonstrate the benefits of accreditation and Call to action for current users to gain accreditation.
• Call to action for attending monthly webinars
• Ability to review past webinars, whitepapers etc.

```html
<!DOCTYPE html>
<html lang="en">
<head>
<meta charset="utf-8">
<title>Talvoro — Project Management Software</title>
<link rel="stylesheet" href="https://fonts.googleapis.com/css2?family=Roboto:wght@300;400;700;900&family=Arimo:wght@400;700&display=swap">
<style>
:root{
  --orange:#f26522;
  --orange-dark:#c94d12;
  --red:#d9332a;
  --ink:#2a2a2a;
  --grey-text:#777;
  --light-grey:#f3f3f3;
  --panel:#2b2b2b;
  --band:#6a6a6a;
  --footer:#575757;
  --nav:#0d0f1a;
  --white:#fff;
}
*{box-sizing:border-box;margin:0;padding:0}
html,body{width:900px;height:1200px;overflow:hidden}
body{position:relative;background:var(--light-grey);font-family:Arimo,Arial,sans-serif;color:var(--ink)}
.abs{position:absolute}
.btn{position:absolute;display:flex;align-items:center;justify-content:center;background:var(--orange);color:var(--white);border-bottom:2px solid var(--orange-dark);font-family:Arimo,Arial,sans-serif}
.btn-dark{background:#1e1e1e;border-bottom:2px solid #000}

/* hero */
.hero{left:0;top:0;width:900px;height:345px;
  background:
    radial-gradient(ellipse 220px 140px at 560px 130px,rgba(60,110,150,.55),transparent),
    radial-gradient(ellipse 260px 160px at 180px 250px,rgba(110,60,140,.45),transparent),
    radial-gradient(ellipse 200px 120px at 820px 300px,rgba(40,60,130,.6),transparent),
    linear-gradient(180deg,#12194a 0%,#1d2a5e 45%,#2a2a5a 100%)}
.logo{left:150px;top:16px}
.logo-name{font-family:Roboto,Arial,sans-serif;font-weight:400;font-size:26px;color:var(--white);letter-spacing:.5px}
.social{display:flex;gap:5px}
.social span{width:13px;height:13px;border-radius:50%;background:#d8d8d8;display:block}
.top-social{left:591px;top:14px}
.login{left:679px;top:16px;font-size:9px;color:#ddd}
.signup{left:705px;top:11px;width:46px;height:19px;font-size:9.5px;border-bottom:none}
.hero-art{left:165px;top:112px;width:325px;height:192px;border-radius:4px;
  background:radial-gradient(ellipse at 35% 60%,#d32a22 0%,#a81d18 40%,rgba(200,200,200,.25) 75%,transparent 100%)}
.hero-copy{right:185px;top:88px;text-align:right;color:var(--white);font-family:Roboto,Arial,sans-serif}
.hero-copy .l1{font-weight:300;font-size:30px;line-height:34px}
.hero-copy .l2{font-weight:400;font-size:18px;line-height:24px}
.hero-copy .l3{font-weight:300;font-size:31px;line-height:38px}
.hero-cta{left:604px;top:217px;width:109px;height:38px;font-size:16px;font-family:Roboto,Arial,sans-serif}
.hero-arrow{top:145px}
.dots{left:704px;top:322px;display:flex;gap:4px}
.dots span{width:9px;height:9px;border-radius:50%;border:1px solid #ddd}
.dots span.on{background:#fff}

/* nav */
.main-nav{left:0;top:345px;width:900px;height:42px;background:var(--nav);border-bottom:1px solid #000}
.main-nav ul{list-style:none;position:absolute;left:150px;width:602px;top:0;height:42px;display:flex;justify-content:space-between;align-items:center}
.main-nav li{font-size:9.5px;color:#aab;}
.main-nav li.active{color:#fff}
.main-nav .sep{width:1px;height:12px;border-left:1px dashed #555}

/* welcome */
.welcome-rule{left:275px;width:348px;height:0;border-top:1px dashed #bbb}
.welcome-title{left:0;width:900px;top:418px;text-align:center;font-family:Roboto,Arial,sans-serif;font-weight:900;font-size:30px;color:#6a6a6a;letter-spacing:.5px}
.welcome-title b{color:#1a1a1a}
.welcome-text{left:148px;width:604px;top:469px;text-align:center;font-size:7.2px;line-height:12px;color:var(--grey-text)}
.welcome-cta{left:415px;top:515px;width:70px;height:24px;font-size:9.5px}

/* features */
.band{left:0;top:573px;width:900px;height:154px;background:var(--band)}
.band-line{left:0;top:568px;width:900px;height:5px;background:var(--orange)}
.feature{top:562px;width:147px;height:165px;background:var(--panel);color:var(--white);text-align:center}
.feature svg{margin-top:18px}
.feature h3{font-weight:400;font-size:10px;margin-top:3px}
.feature p{text-align:left;font-size:7px;line-height:12px;color:#aaa;padding:0 6px;margin-top:13px;height:58px}
.feature .btn{left:50%;transform:translateX(-50%);top:132px;width:54px;height:18px;font-size:7.5px}
.shadow-rule{left:150px;width:600px;height:3px;background:radial-gradient(ellipse at center,rgba(0,0,0,.25),transparent 70%)}

/* blog */
.section-title{font-family:Roboto,Arial,sans-serif;font-weight:400;font-size:17px;color:#1e1e1e}
.section-title span{color:#888}
.post-head{left:151px;display:flex;align-items:flex-end;gap:7px}
.post-date{font-size:10px;color:#aaa;line-height:8px;text-align:center}
.post-date small{display:block;font-size:5px}
.post-title{font-family:Roboto,Arial,sans-serif;font-size:15px;color:#666}
.post-meta{left:150px;font-size:7px;color:#888}
.post-meta a{color:var(--orange);text-decoration:none}
.thumb{left:151px;width:74px;height:52px;border:2px solid #ddd;box-shadow:0 0 0 1px #999;background:linear-gradient(135deg,#2d3b5a,#8a8fa0 55%,#4a5a7a)}
.post-text{left:237px;width:290px;font-size:7px;line-height:10.5px;color:#777}
.read{left:237px;font-size:7.5px;color:#333}
.dash{height:0;border-top:1px dashed #bbb}
.view-more{width:54px;height:19px;font-size:7.5px}

/* news */
.news-item{left:588px;width:162px;display:flex;gap:8px}
.news-date{width:26px;height:25px;background:var(--red);color:#fff;text-align:center;flex:none;font-size:10px;line-height:11px;padding-top:2px}
.news-date small{display:block;font-size:6px;line-height:7px}
.news-text{font-size:7px;line-height:9px;color:#777}
.news-text a{color:var(--red);display:block}

/* newsletter */
.subscribe-title{left:250px;top:1030px;font-family:Roboto,Arial,sans-serif;font-weight:300;font-size:18px;color:#333}
.subscribe-title span{color:#888}
.email-field{left:250px;top:1054px;width:294px;height:31px;background:#fff;border:1px solid #ccc;font-size:8px;color:#666;padding:10px 9px}
.subscribe-btn{left:543px;top:1054px;width:106px;height:31px;font-family:Roboto,Arial,sans-serif;font-weight:300;font-size:18px;border-bottom:none}

/* footer */
.footer{left:0;top:1090px;width:900px;height:110px;background:var(--footer)}
.foot-title{font-size:9.5px;color:#fff}
.foot-list{list-style:none;font-size:7px;line-height:12px;color:#ccc}
.team li{list-style:disc;margin-left:10px}
.foot-social{left:680px;top:1098px}
.foot-social span{background:#e0e0e0}
.free-trial{left:625px;top:1125px;width:126px;height:32px;font-family:Roboto,Arial,sans-serif;font-weight:300;font-size:17px;background:#1c1c1c;border:1px solid #777;border-bottom:3px solid #000}
.copyright{left:0;width:900px;top:1182px;text-align:center;font-size:7px;color:#ccc}
</style>
</head>
<body>

<section class="abs hero">
  <div class="abs logo"><span class="logo-name">talvoro</span></div>
  <div class="abs social top-social"><span></span><span></span><span></span><span></span></div>
  <div class="abs login">Login</div>
  <div class="btn signup">SignUp</div>

  <div class="abs hero-art" role="img" aria-label="Illustration of figures passing red blocks up a staircase of blocks"></div>

  <div class="abs hero-copy">
    <div class="l1">Project Management</div>
    <div class="l2">Simple, Easy to use</div>
    <div class="l3">Project Management Software</div>
  </div>
  <div class="btn hero-cta">Learn more</div>

  <svg class="abs hero-arrow" style="left:120px" width="32" height="62" viewBox="0 0 32 62"><polyline points="30,1 2,31 30,61" fill="none" stroke="#dde" stroke-width="1.3"/></svg>
  <svg class="abs hero-arrow" style="left:750px" width="32" height="62" viewBox="0 0 32 62"><polyline points="2,1 30,31 2,61" fill="none" stroke="#dde" stroke-width="1.3"/></svg>

  <div class="abs dots"><span class="on"></span><span></span><span></span><span></span></div>
</section>

<nav class="abs main-nav">
  <ul>
    <li class="active">Products and Services</li><li class="sep"></li>
    <li>About Us</li><li class="sep"></li>
    <li>News and Events</li><li class="sep"></li>
    <li>Maturity Self Testing</li><li class="sep"></li>
    <li>Blog</li><li class="sep"></li>
    <li>Accreditation</li><li class="sep"></li>
    <li>Our Uniqueness</li>
  </ul>
</nav>

<div class="abs welcome-rule" style="top:414px"></div>
<div class="abs welcome-rule" style="top:416px"></div>
<h1 class="abs welcome-title">WELCOME TO <b>TALVORO</b></h1>
<div class="abs welcome-rule" style="top:456px"></div>
<div class="abs welcome-rule" style="top:458px"></div>
<p class="abs welcome-text">Lorem ipsum dolor sit amet, consectetur adipiscing elit. Sed ultrices pulvinar consequat. Vivamus ornare, nisi eu dapibus scelerisque, diam dolor pretium dolor, sit amet sodales lorem sapien vel ante. Sed lacus sapien, varius sit amet elementum vulputate, adipiscing id ligula. Maecenas in sapien sit amet urna condimentum eleifend ac interdum lorem. Sed placerat rhoncus arcu, non scelerisque lectus dictum ac. Morbi sit amet dictum magna.</p>
<div class="btn welcome-cta">Read more</div>

<div class="abs band-line"></div>
<div class="abs band"></div>

<article class="abs feature" style="left:150px">
  <svg width="16" height="15" viewBox="0 0 16 15"><circle cx="6" cy="4" r="3" fill="#fff"/><path d="M0 14c0-4 3-6 6-6s6 2 6 6z" fill="#fff"/><circle cx="11" cy="3.5" r="2.5" fill="#fff"/><path d="M12 7c2 .5 4 2 4 5h-3" fill="#fff"/></svg>
  <h3>Project Management</h3>
  <p>Simple, easy to use project management software. Plan, Track and Improve your projects. Reduce costs and increase efficiency.</p>
  <div class="btn">Learn more</div>
</article>
<article class="abs feature" style="left:301px">
  <svg width="16" height="16" viewBox="0 0 16 16"><circle cx="8" cy="8" r="6.5" fill="none" stroke="#fff" stroke-width="1.6"/><polyline points="8,4 8,8 11,10" fill="none" stroke="#fff" stroke-width="1.5"/></svg>
  <h3>Timesheets</h3>
  <p>Powerful hosted project time and status collection. Track expenses and time. Have an audit trail on your time billing. Timesheet software</p>
  <div class="btn">Learn more</div>
</article>
<article class="abs feature" style="left:453px">
  <svg width="16" height="16" viewBox="0 0 16 16"><circle cx="6" cy="10" r="4" fill="none" stroke="#fff" stroke-width="2.4" stroke-dasharray="2 1.4"/><circle cx="12" cy="4" r="2.6" fill="none" stroke="#fff" stroke-width="1.8" stroke-dasharray="1.4 1"/></svg>
  <h3>Resource Management</h3>
  <p>Plan, manage and control work for your whole organisation or a single project. Resource management</p>
  <div class="btn">Learn more</div>
</article>
<article class="abs feature" style="left:603px">
  <svg width="16" height="16" viewBox="0 0 16 16"><path d="M13 6A5.5 5.5 0 0 0 3 5" fill="none" stroke="#fff" stroke-width="1.8"/><path d="M3 10a5.5 5.5 0 0 0 10 1" fill="none" stroke="#fff" stroke-width="1.8"/><polygon points="14,1 14,7 9,6" fill="#fff"/><polygon points="2,15 2,9 7,10" fill="#fff"/></svg>
  <h3>Issues, Risks and change</h3>
  <p>Track and report on issues, risk and change. One click reports. issue management</p>
  <div class="btn">Learn more</div>
</article>
<div class="abs shadow-rule" style="top:727px"></div>

<h2 class="abs section-title" style="left:151px;top:755px">BLOG</h2>

<div class="abs post-head" style="top:781px"><div class="post-date">05<small>JUL</small></div><div class="post-title">Lorem ipsum dolor</div></div>
<div class="abs post-meta" style="top:802px">Posted By: <a>TALVORO</a> &nbsp;|&nbsp; <a>30 Comments</a></div>
<div class="abs thumb" style="top:814px" role="img" aria-label="Blog post thumbnail photo"></div>
<p class="abs post-text" style="top:814px">Lorem ipsum dolor sit amet, consectetur adipiscing elit. Maecenas varius pellentesque dapibus. Praesent et dui justo. Cras porttitor posuere orci, eu ultrices enim faucibus quis consectetur adipiscing elit. Maecenas varius pellentesque dapibus. Praesent et dui justo</p>
<div class="abs read" style="top:860px">Read more...</div>
<div class="abs dash" style="left:150px;width:375px;top:878px"></div>

<div class="abs post-head" style="top:888px"><div class="post-date">05<small>JUL</small></div><div class="post-title">Lorem ipsum dolor</div></div>
<div class="abs post-meta" style="top:909px">Posted By: <a>TALVORO</a> &nbsp;|&nbsp; <a>30 Comments</a></div>
<div class="abs thumb" style="top:922px;background:linear-gradient(135deg,#dfe3ea,#5a7bb0 50%,#e8ebf0)" role="img" aria-label="Blog post thumbnail photo"></div>
<p class="abs post-text" style="top:921px">Lorem ipsum dolor sit amet, consectetur adipiscing elit. Maecenas varius pellentesque dapibus. Praesent et dui justo. Cras porttitor posuere orci, eu ultrices enim faucibus quis consectetur adipiscing elit. Maecenas varius pellentesque dapibus. Praesent et dui justo</p>
<div class="abs read" style="top:967px">Read more...</div>
<div class="btn btn-dark view-more" style="left:150px;top:984px">View more</div>

<h2 class="abs section-title" style="left:588px;top:755px">NEWS <span>&amp; EVENTS</span></h2>
<div class="abs news-item" style="top:787px"><div class="news-date">05<small>JUL</small></div><div class="news-text">Lorem ipsum dolor sit amet, consectetur adipiscing elit. Sed ultrices pulvinar consequat. Vivamus ornare. <a>Read more</a></div></div>
<div class="abs dash" style="left:588px;width:162px;top:834px"></div>
<div class="abs news-item" style="top:847px"><div class="news-date">05<small>JUL</small></div><div class="news-text">Lorem ipsum dolor sit amet, consectetur adipiscing elit. Sed ultrices pulvinar consequat. Vivamus ornare. <a>Read more</a></div></div>
<div class="abs dash" style="left:588px;width:162px;top:894px"></div>
<div class="abs news-item" style="top:907px"><div class="news-date">05<small>JUL</small></div><div class="news-text">Lorem ipsum dolor sit amet, consectetur adipiscing elit. Sed ultrices pulvinar consequat. Vivamus ornare. <a>Read more</a></div></div>
<div class="btn btn-dark view-more" style="left:588px;top:984px">View more</div>

<div class="abs shadow-rule" style="top:1010px"></div>

<h2 class="abs subscribe-title">Subscribe <span>to our Newsletter</span></h2>
<div class="abs email-field">Enter your email...</div>
<div class="btn subscribe-btn">Subscribe</div>

<footer class="abs footer"></footer>
<div class="abs foot-title" style="left:149px;top:1098px">Navigation</div>
<ul class="abs foot-list" style="left:150px;top:1117px"><li>Home</li><li>FAQ</li><li>Support &amp; Training</li><li>Contact Us</li></ul>
<ul class="abs foot-list" style="left:276px;top:1118px"><li>Tour</li><li>Features</li><li>Pricing</li><li>Sign up</li></ul>
<ul class="abs foot-list" style="left:370px;top:1118px"><li>Careers</li><li>Privacy Policy</li><li>Terms of Sale</li><li>Sitemap</li></ul>
<div class="abs foot-title" style="left:482px;top:1098px">Team Members</div>
<ul class="abs foot-list team" style="left:482px;top:1121px"><li>Nigel Brask</li><li>Dorian Felsk</li><li>Ansel Quorry</li></ul>
<div class="abs social foot-social"><span></span><span></span><span></span><span></span></div>
<div class="btn free-trial">Free Trial</div>
<div class="abs copyright">© 2003 - 2012 talvoro pty. ltd. All Rights Reserved</div>

</body>
</html>
```